New locally owned rental company needs a flyer to circulate

Need flyer with logo, phone# and address. We rent cars to anyone with driver's license and proper insurance. Rates as low as $50/day. Can offer compact cars, mid-size and full size sedans. Also SUV's.

```html
<!DOCTYPE html>
<html lang="en">
<head>
<meta charset="utf-8">
<title>DriveReady Car &amp; Van Rental Flyer</title>
<link href="https://fonts.googleapis.com/css2?family=Poppins:ital,wght@0,400;0,500;0,700;0,800;0,900;1,700;1,800;1,900&display=swap" rel="stylesheet">
<style>
  :root {
    --blue: #0b4fb0;
    --green: #2bb24c;
    --dark: #1d1d1d;
    --ink: #222222;
    --white: #ffffff;
    --page: #c4c4c4;
  }
  * { margin: 0; padding: 0; box-sizing: border-box; }
  html, body { width: 1200px; height: 1080px; overflow: hidden; }
  body { background: var(--page); font-family: "Poppins", sans-serif; }

  .flyer {
    position: absolute; left: 200px; top: 22px;
    width: 800px; height: 1035px;
    background: var(--dark); overflow: hidden;
  }
  .hero-photo {
    position: absolute; left: 0; top: 0; width: 800px; height: 345px;
    background: linear-gradient(180deg, #f4f6f8 0%, #dfe4ea 45%, #8a8f95 70%, #5b5550 100%);
  }
  .hero-photo::after {
    content: ""; position: absolute; left: 0; right: 0; bottom: 0; height: 110px;
    background: linear-gradient(90deg, #6f7376 0%, #a83336 25%, #2a2a2c 50%, #a83336 70%, #6f7376 100%);
    opacity: .55;
  }
  .brand { position: absolute; left: 68px; top: 62px; }
  .brand-name {
    font-weight: 800; font-size: 50px; line-height: 1; color: var(--blue); letter-spacing: -1px;
  }
  .brand-tagline {
    margin-top: 12px; margin-left: 36px;
    font-weight: 800; font-style: italic; font-size: 22px; letter-spacing: 9px; color: #111;
  }

  .ribbon {
    position: absolute; left: -20px; width: 860px; height: 30px;
    font-weight: 800; font-style: italic; font-size: 19px; color: var(--white);
    white-space: nowrap; line-height: 30px; overflow: hidden;
  }
  .ribbon-green { top: 318px; background: var(--green); transform: rotate(-2deg); }
  .ribbon-blue { top: 335px; background: var(--blue); transform: rotate(2deg); }

  .offer-band { position: absolute; left: 0; top: 0; width: 800px; height: 1035px; }

  .headline {
    position: absolute; left: 54px; top: 418px;
    font-weight: 900; font-style: italic; font-size: 68px; letter-spacing: -2px; line-height: 1;
    color: var(--blue); -webkit-text-stroke: 2px var(--white); paint-order: stroke fill;
  }
  .headline .accent { color: var(--green); }
  .intro { position: absolute; left: 60px; top: 505px; font-size: 22px; color: var(--white); }
  .requirements { position: absolute; left: 56px; top: 548px; list-style: none; }
  .requirements li {
    display: flex; align-items: center; gap: 12px; height: 48px;
    font-weight: 800; font-style: italic; font-size: 32px; color: var(--white);
  }
  .requirements .amp { color: var(--green); font-style: normal; font-weight: 500; margin-left: 8px; }

  .price-card {
    position: absolute; left: 490px; top: 350px; width: 270px; height: 318px;
    background: var(--white); transform: rotate(2.5deg);
    box-shadow: 0 6px 16px rgba(0,0,0,.35); padding: 8px;
  }
  .price-inner { position: relative; width: 100%; height: 100%; border: 2px solid var(--blue); overflow: hidden; }
  .price-photo {
    position: absolute; inset: 0;
    background: linear-gradient(160deg, #f1f2f4 0%, #c9ccd2 40%, #6c7078 70%, #f5f5f5 100%);
  }
  .price-disc {
    position: absolute; left: 120px; top: 95px; width: 170px; height: 200px;
    border-radius: 50%; background: var(--green);
  }
  .price-amount {
    position: absolute; left: 18px; top: 128px;
    font-weight: 900; font-style: italic; font-size: 92px; letter-spacing: -3px; line-height: 1;
    color: var(--blue); -webkit-text-stroke: 3px var(--white); paint-order: stroke fill;
  }
  .price-note { position: absolute; left: 24px; top: 258px; font-size: 13px; color: var(--ink); }
  .price-unit {
    position: absolute; left: 160px; top: 246px;
    font-weight: 900; font-style: italic; font-size: 24px; color: var(--blue);
    -webkit-text-stroke: 1.5px var(--white); paint-order: stroke fill;
  }

  .fleet-grid {
    position: absolute; left: 54px; top: 668px; width: 390px; height: 224px;
    display: grid; grid-template-columns: 1fr 1fr; grid-template-rows: 1fr 1fr; gap: 6px;
  }
  .fleet-photo { border: 3px solid var(--white); box-shadow: 0 3px 8px rgba(0,0,0,.3); }
  .fleet-grey { background: linear-gradient(180deg, #b9c7d6 0%, #6d7175 55%, #8c8e86 100%); }
  .fleet-blue { background: linear-gradient(180deg, #c8d2dc 0%, #2a3fb0 55%, #8e8a84 100%); }
  .fleet-red { background: linear-gradient(180deg, #d6dbe0 0%, #b52532 55%, #6f6a64 100%); }
  .fleet-silver { background: linear-gradient(180deg, #d9c9b4 0%, #b6b8bb 55%, #5e5e5e 100%); }

  .offers { position: absolute; left: 486px; top: 700px; }
  .offers-title {
    font-weight: 900; font-style: italic; font-size: 32px; letter-spacing: -1px; color: var(--blue);
  }
  .offers-list { list-style: none; margin-top: 6px; }
  .offers-list li {
    display: flex; align-items: center; gap: 14px; height: 31px;
    font-size: 23px; color: var(--ink);
  }
  .offers-list li::before { content: ""; width: 6px; height: 6px; background: var(--blue); margin-top: 6px; }

  .contact { position: absolute; left: 62px; top: 928px; display: flex; align-items: center; }
  .phone {
    display: flex; align-items: center; gap: 12px;
    font-weight: 900; font-style: italic; font-size: 44px; color: var(--white); letter-spacing: -1px;
  }
  .address {
    display: flex; align-items: center; gap: 12px; margin-left: 28px;
    font-size: 14px; line-height: 1.3; color: var(--white);
  }
</style>
</head>
<body>
  <main class="flyer">
    <div class="hero-photo" role="img" aria-label="Photo of rental sedans parked in front of a white rental office building"></div>

    <svg class="offer-band" viewBox="0 0 800 1035" aria-hidden="true">
      <polygon points="0,687 800,630 800,884 0,934" fill="#ffffff"/>
    </svg>

    <div class="brand">
      <div class="brand-name">DriveReady</div>
      <div class="brand-tagline">Car &amp; Van Rental</div>
    </div>

    <div class="ribbon ribbon-green">&nbsp;CAR RENTAL · CAR RENTAL · CAR RENTAL · CAR RENTAL · CAR RENTAL · CAR RENTAL · CAR RENTAL</div>
    <div class="ribbon ribbon-blue">&nbsp;CAR RENTAL · CAR RENTAL · CAR RENTAL · CAR RENTAL · CAR RENTAL · CAR RENTAL · CAR RENTAL</div>

    <h1 class="headline">Need <span class="accent">a car?</span></h1>
    <p class="intro">We rent cars to anyone with</p>
    <ul class="requirements">
      <li>
        <svg width="30" height="34" viewBox="0 0 30 34" aria-hidden="true"><rect x="2" y="8" width="22" height="22" fill="#fff"/><path d="M7 18 L13 25 L28 2" stroke="#0b4fb0" stroke-width="4" fill="none"/></svg>
        <span>DRIVER'S LICENSE<span class="amp">&amp;</span></span>
      </li>
      <li>
        <svg width="30" height="34" viewBox="0 0 30 34" aria-hidden="true"><rect x="2" y="8" width="22" height="22" fill="#fff"/><path d="M7 18 L13 25 L28 2" stroke="#0b4fb0" stroke-width="4" fill="none"/></svg>
        <span>PROPER INSURANCE</span>
      </li>
    </ul>

    <div class="price-card">
      <div class="price-inner">
        <div class="price-photo" role="img" aria-label="Photo of a hand holding out car keys"></div>
        <div class="price-disc"></div>
        <div class="price-amount">$50</div>
        <div class="price-note">Rates as low as</div>
        <div class="price-unit">/DAY</div>
      </div>
    </div>

    <div class="fleet-grid">
      <div class="fleet-photo fleet-grey" role="img" aria-label="Photo of a grey SUV"></div>
      <div class="fleet-photo fleet-blue" role="img" aria-label="Photo of a blue sedan"></div>
      <div class="fleet-photo fleet-red" role="img" aria-label="Photo of a red compact sedan"></div>
      <div class="fleet-photo fleet-silver" role="img" aria-label="Photo of a silver SUV"></div>
    </div>

    <section class="offers">
      <h2 class="offers-title">WE CAN OFFER:</h2>
      <ul class="offers-list">
        <li>compact cars</li>
        <li>mid-size sedans</li>
        <li>full size sedans</li>
        <li>SUV</li>
      </ul>
    </section>

    <footer class="contact">
      <div class="phone">
        <svg width="26" height="28" viewBox="0 0 24 24" aria-hidden="true"><path fill="#0b4fb0" d="M6.6 10.8a15.1 15.1 0 0 0 6.6 6.6l2.2-2.2c.3-.3.7-.4 1-.2 1.1.4 2.3.6 3.6.6.6 0 1 .4 1 1V20c0 .6-.4 1-1 1A17 17 0 0 1 3 4c0-.6.4-1 1-1h3.5c.6 0 1 .4 1 1 0 1.3.2 2.5.6 3.6.1.3 0 .7-.2 1z"/></svg>
        <span>256-555-0142</span>
      </div>
      <div class="address">
        <svg width="20" height="26" viewBox="0 0 20 26" aria-hidden="true"><path d="M10 1C5 1 1.5 4.8 1.5 9.5 1.5 16 10 25 10 25s8.5-9 8.5-15.5C18.5 4.8 15 1 10 1z" fill="#fff" stroke="#0b4fb0" stroke-width="2"/><circle cx="10" cy="9.5" r="3.2" fill="#0b4fb0"/></svg>
        <span>4870 Oakline Boulevard<br>Riverton, AL 35800</span>
      </div>
    </footer>
  </main>
</body>
</html>
```